Letter Head for accounting firm

We need letter head designed using our attached logo.

We also need the following information on the letterhead:

482 E Mill Rd. Danvers, OH 43762

HarborLedgerLtd.com

1-855-613-2907

Contact Information for Business Card

Use logo

Colors

Designer to choose colors to be used in the design.

Requirements
Must have
• Business Card - Should also have name and title - email address

```html
<!DOCTYPE html>
<html lang="en">
<head>
<meta charset="utf-8">
<title>Harbor Ledger Group LTD — Business Card</title>
<link rel="stylesheet" href="https://fonts.googleapis.com/css2?family=Raleway:wght@400;600;700&display=swap">
<style>
  :root {
    --backdrop: #2a2a2b;
    --card: #1d1f22;
    --card-back: #1a1b1d;
    --pattern: #262729;
    --brand-blue: #1e86d0;
    --ink: #e9eaec;
    --ink-soft: #c9cbce;
    --rule: #6b6e73;
  }
  * { margin: 0; padding: 0; box-sizing: border-box; }
  html, body { width: 1200px; height: 1108px; overflow: hidden; }
  body {
    background: var(--backdrop);
    font-family: "Raleway", sans-serif;
    position: relative;
  }
  .card {
    position: absolute;
    top: 184px;
    width: 460px;
    height: 740px;
    border-radius: 26px;
    overflow: hidden;
  }
  .card-front { left: 110px; background: var(--card); text-align: center; color: var(--ink); }
  .card-back { left: 630px; background: var(--card-back); }

  .brand-mark {
    width: 92px; height: 92px;
    margin: 86px auto 0;
    background: var(--brand-blue);
  }
  .brand-name {
    margin-top: 26px;
    font-size: 27px;
    font-weight: 700;
    letter-spacing: 0.5px;
    color: var(--brand-blue);
  }
  .brand-rule {
    position: relative;
    width: 320px;
    margin: 10px auto 0;
    height: 14px;
  }
  .brand-rule::before {
    content: ""; position: absolute; left: 0; right: 0; top: 7px;
    border-top: 1.5px solid var(--rule);
  }
  .brand-rule span {
    position: relative;
    background: var(--card);
    padding: 0 8px;
    font-size: 12px;
    font-weight: 700;
    letter-spacing: 2px;
    color: var(--ink);
    line-height: 14px;
  }
  .person-name {
    margin-top: 40px;
    font-size: 27px;
    font-weight: 700;
    color: var(--brand-blue);
    letter-spacing: 0.5px;
  }
  .person-title {
    margin-top: 6px;
    font-size: 17px;
    font-weight: 400;
    letter-spacing: 1px;
    color: var(--ink-soft);
  }
  .contact-divider {
    display: flex; align-items: center; justify-content: center;
    gap: 10px;
    width: 300px; margin: 26px auto 0;
  }
  .contact-divider .line { flex: 1; border-top: 1.5px solid var(--rule); }
  .contact-divider svg { width: 26px; height: 26px; display: block; }
  .contact-list { margin-top: 14px; list-style: none; }
  .contact-list li {
    font-size: 18px;
    line-height: 30px;
    letter-spacing: 0.6px;
    color: var(--ink);
  }
  .address-rule { width: 300px; margin: 20px auto 0; border-top: 1.5px solid var(--rule); }
  .address {
    margin-top: 18px;
    font-size: 18px;
    line-height: 30px;
    font-style: normal;
    letter-spacing: 0.6px;
    color: var(--ink);
  }

  .back-pattern {
    position: absolute; inset: 0;
    background: linear-gradient(160deg, var(--pattern) 0%, var(--card-back) 75%);
  }
  .back-brand {
    position: absolute;
    left: 50px; bottom: 94px;
    width: 330px;
  }
  .back-brand .brand-name { margin-top: 0; color: var(--ink); text-align: left; }
  .back-brand .brand-rule { margin: 10px 0 0; text-align: center; }
  .back-brand .brand-rule span { background: var(--card-back); }
</style>
</head>
<body>
  <section class="card card-front">
    <div class="brand-mark"></div>
    <div class="brand-name">HARBOR LEDGER GROUP</div>
    <div class="brand-rule"><span>LTD</span></div>

    <div class="person-name">DANIEL MORROW</div>
    <div class="person-title">MANAGING DIRECTOR</div>

    <div class="contact-divider">
      <span class="line"></span>
      <svg viewBox="0 0 26 26" aria-label="Phone">
        <circle cx="13" cy="13" r="13" fill="#1e86d0"/>
        <path d="M9 7.5c.6-.6 1.4-.5 1.8.2l1 1.7c.3.6.2 1.2-.3 1.6l-.7.6c.6 1.4 1.6 2.5 3 3.1l.6-.7c.4-.5 1-.6 1.6-.3l1.7 1c.7.4.8 1.2.2 1.8l-.9.9c-.8.8-2.1.9-3.4.3-2.5-1.2-4.4-3.1-5.6-5.6-.6-1.3-.5-2.6.3-3.4z" fill="#1d1f22"/>
      </svg>
      <svg viewBox="0 0 26 26" aria-label="Email">
        <circle cx="13" cy="13" r="13" fill="#1e86d0"/>
        <rect x="7" y="8.5" width="12" height="9" rx="1" fill="#1d1f22"/>
        <path d="M7.5 9.2l5.5 4.3 5.5-4.3" fill="none" stroke="#1e86d0" stroke-width="1.3"/>
      </svg>
      <svg viewBox="0 0 26 26" aria-label="Website">
        <circle cx="13" cy="13" r="13" fill="#1e86d0"/>
        <circle cx="13" cy="13" r="6" fill="none" stroke="#1d1f22" stroke-width="1.5"/>
        <ellipse cx="13" cy="13" rx="2.6" ry="6" fill="none" stroke="#1d1f22" stroke-width="1.3"/>
        <path d="M7 13h12" stroke="#1d1f22" stroke-width="1.3"/>
      </svg>
      <span class="line"></span>
    </div>

    <ul class="contact-list">
      <li>1-855-613-2907</li>
      <li>INFO@HARBORLEDGERLTD.COM</li>
      <li>WWW.HARBORLEDGERLTD.COM</li>
    </ul>

    <div class="address-rule"></div>
    <address class="address">482 E MILL RD. DANVERS<br>OH 43762</address>
  </section>

  <section class="card card-back">
    <div class="back-pattern" role="img" aria-label="Faint repeating brand-mark pattern across the card back"></div>
    <div class="back-brand">
      <div class="brand-name">HARBOR LEDGER GROUP</div>
      <div class="brand-rule"><span>LTD</span></div>
    </div>
  </section>
</body>
</html>
```